Solar Energy Company Flyer/Door Hanger

Hello designers,

We are a solar energy company looking to make an eye-catching design for residential door hangers. These will be the type of door hangers that just stick to the door, not actually hang on the door. So essentially it will be a flyer that is 5.5" x 8.5" front and back. Please see attached template design for specifications and standards for print. The file will need to be provided in an editable PSD format.

Content for Flyer:

Front: Should be something eye caching, attention grabber, with big words and a visual of something to do with a nice looking home that has solar panels on it. Call to action should be at the bottom.

Words should ready: MAKE CENTS OUT OF SOLAR

Call to action link: apply.vendrilux.com

Back: Should have more in depth content. Company logo on back, 4 bullet points (checkmarks) with text, a chart (attached), and contact info at bottom. We will update content for the back soon, but please put together a layout that doesn't look plain jane and has some creativeness to it.

Update on content will be soon. If you want you can submit the front first and the back after.

Thanks!

Reason: Giving more time for our team to look over and see more designs!

Target Market(s)

Residential Home Owners

Industry/Entity Type

Solar Energy

Requirements
Must have
• Front should be clean and eycatching, back should be creative yet informational

```html
<!DOCTYPE html>
<html lang="en">
<head>
<meta charset="utf-8">
<title>Vendrilux Solar – Flyer Front and Back</title>
<link href="https://fonts.googleapis.com/css2?family=Roboto+Condensed:wght@700&family=Roboto:wght@400;700&family=Montserrat:wght@700&display=swap" rel="stylesheet">
<style>
  :root {
    --stage: #000000;
    --paper: #ffffff;
    --forest: #136b3a;
    --lime: #a9cc2e;
    --sage: #9cbf7e;
    --ink: #111111;
    --slate: #8a9eaa;
    --grey-text: #777777;
  }
  * { margin: 0; padding: 0; box-sizing: border-box; }
  html, body { width: 1200px; height: 999px; overflow: hidden; background: var(--stage); }
  .canvas { position: relative; width: 1200px; height: 999px; background: var(--stage); }

  .flyer { position: absolute; top: 70px; width: 555px; height: 858px; background: var(--paper); overflow: hidden; }
  .flyer--front { left: 45px; }
  .flyer--back { left: 623px; font-family: "Roboto", Arial, sans-serif; }

  .front-art { position: absolute; inset: 0; width: 555px; height: 858px; }
  .headline { font-family: "Roboto Condensed", "Arial Narrow", sans-serif; font-weight: 700; fill: var(--forest); }
  .cta-link { font-family: "Montserrat", Arial, sans-serif; font-weight: 700; fill: var(--ink); font-size: 19px; letter-spacing: 4px; }

  .brand { position: absolute; top: 272px; left: 0; width: 555px; text-align: center; }
  .brand__name { font-size: 36px; font-weight: 700; color: var(--ink); }

  .benefits { position: absolute; left: 27px; top: 391px; width: 502px; height: 156px; background: var(--forest); border-radius: 5px; color: var(--paper); padding: 10px 16px; }
  .benefits__title { font-size: 21px; font-weight: 700; margin-bottom: 6px; }
  .benefits__list { list-style: none; }
  .benefits__item { display: flex; align-items: center; gap: 12px; font-size: 14px; height: 28.5px; }
  .benefits__tick { width: 14px; height: 14px; flex: none; }

  .savings-chart { position: absolute; left: 160px; top: 563px; width: 250px; height: 140px; }
  .chart-label { font-family: "Roboto Condensed", "Arial Narrow", sans-serif; font-weight: 700; font-size: 8px; letter-spacing: 0.5px; }
  .chart-savings { font-family: "Roboto Condensed", "Arial Narrow", sans-serif; font-weight: 700; font-size: 13px; fill: var(--forest); }
  .chart-axis { font-size: 8px; fill: var(--grey-text); }

  .contact { position: absolute; left: 26px; top: 722px; color: var(--ink); }
  .contact__title { font-size: 20px; font-weight: 700; margin-bottom: 10px; }
  .contact__address { font-size: 13px; line-height: 18px; }
  .contact__lines { position: absolute; left: 192px; top: 745px; list-style: none; font-size: 13px; color: var(--ink); }
  .contact__line { display: flex; align-items: center; gap: 10px; height: 17.5px; }
  .contact__icon { width: 13px; height: 13px; flex: none; }

  .cta-bar { position: absolute; left: 0; top: 808px; width: 555px; height: 31px; background: var(--lime); display: flex; align-items: center; justify-content: center; font-family: "Montserrat", Arial, sans-serif; font-weight: 700; font-size: 19px; letter-spacing: 4px; color: var(--ink); }
</style>
</head>
<body>
<div class="canvas">

  <section class="flyer flyer--front">
    <svg class="front-art" viewBox="0 0 555 858" xmlns="http://www.w3.org/2000/svg">
      <defs>
        <linearGradient id="roofTones" x1="0" y1="0" x2="0.6" y2="1">
          <stop offset="0" stop-color="#7fa9d8"/>
          <stop offset="0.3" stop-color="#2e4f9c"/>
          <stop offset="0.75" stop-color="#1d3a86"/>
          <stop offset="1" stop-color="#26478f"/>
        </linearGradient>
      </defs>
      <rect class="band-lime" x="0" y="380" width="555" height="478" fill="#a9cc2e"/>
      <path d="M0,410 Q260,500 555,440 V470 Q260,530 0,440 Z" fill="#9cbf7e"/>
      <path d="M0,420 Q270,520 555,455" fill="none" stroke="#136b3a" stroke-width="7"/>
      <path role="img" aria-label="Photo: installer fitting solar panels on a house roof under a blue sky" d="M0,0 H555 V440 Q280,500 0,410 Z" fill="url(#roofTones)"/>
      <text class="headline" x="40" y="572" font-size="58" textLength="480" lengthAdjust="spacingAndGlyphs">MAKE CENTS OUT OF</text>
      <text class="headline" x="42" y="720" font-size="188" textLength="482" lengthAdjust="spacingAndGlyphs">SOLAR</text>
      <path d="M0,805 Q270,755 555,778 V858 H0 Z" fill="#ffffff"/>
      <path d="M0,805 Q270,755 555,778" fill="none" stroke="#136b3a" stroke-width="6"/>
      <text class="cta-link" x="277" y="825" text-anchor="middle">apply.vendrilux.com</text>
    </svg>
  </section>

  <section class="flyer flyer--back">
    <div class="brand">
      <span class="brand__name">Vendrilux Solar</span>
    </div>

    <div class="benefits">
      <h2 class="benefits__title">Title Here</h2>
      <ul class="benefits__list">
        <li class="benefits__item"><svg class="benefits__tick" viewBox="0 0 14 14"><rect x="1" y="3" width="10" height="10" fill="none" stroke="#fff" stroke-width="1.4"/><path d="M3,7 L6,10 L13,1" fill="none" stroke="#fff" stroke-width="2"/></svg>Lorem ipsum dolor sit amet, consectetur adipiscing elit</li>
        <li class="benefits__item"><svg class="benefits__tick" viewBox="0 0 14 14"><rect x="1" y="3" width="10" height="10" fill="none" stroke="#fff" stroke-width="1.4"/><path d="M3,7 L6,10 L13,1" fill="none" stroke="#fff" stroke-width="2"/></svg>Lorem ipsum dolor sit amet, consectetur adipiscing elit</li>
        <li class="benefits__item"><svg class="benefits__tick" viewBox="0 0 14 14"><rect x="1" y="3" width="10" height="10" fill="none" stroke="#fff" stroke-width="1.4"/><path d="M3,7 L6,10 L13,1" fill="none" stroke="#fff" stroke-width="2"/></svg>Lorem ipsum dolor sit amet, consectetur adipiscing elit</li>
        <li class="benefits__item"><svg class="benefits__tick" viewBox="0 0 14 14"><rect x="1" y="3" width="10" height="10" fill="none" stroke="#fff" stroke-width="1.4"/><path d="M3,7 L6,10 L13,1" fill="none" stroke="#fff" stroke-width="2"/></svg>Lorem ipsum dolor sit amet, consectetur adipiscing elit</li>
      </ul>
    </div>

    <svg class="savings-chart" viewBox="0 0 250 140" xmlns="http://www.w3.org/2000/svg">
      <path d="M5,80 Q110,55 212,12 L218,4 V118 H5 Z" fill="#8a9eaa"/>
      <path d="M5,95 Q110,85 218,60 V118 H5 Z" fill="#9cbf7e"/>
      <path d="M5,107 Q110,102 218,88 V118 H5 Z" fill="#4f8a3a"/>
      <text class="chart-label" fill="#333" transform="translate(18,80) rotate(-14)">UTILITY BILL WITHOUT SOLAR</text>
      <text class="chart-label" fill="#fff" x="20" y="99">SOLAR PAYMENT</text>
      <text class="chart-label" fill="#fff" x="20" y="114">UTILITY BILL WITH SOLAR</text>
      <text class="chart-savings" transform="translate(234,60) rotate(-90)">SAVINGS</text>
      <text class="chart-axis" x="4" y="132">Year 1</text>
      <text class="chart-axis" x="98" y="132">Year 10</text>
      <text class="chart-axis" x="194" y="132">Year 20</text>
    </svg>

    <div class="contact">
      <h3 class="contact__title">contact info</h3>
      <p class="contact__address">suit # 00, Lorem Ipsum<br>Lorem Lorem Ipsum</p>
    </div>
    <ul class="contact__lines">
      <li class="contact__line"><svg class="contact__icon" viewBox="0 0 14 14"><path d="M3,1 L5,1 L6,4 L4.5,5.5 Q6,8.5 8.5,9.5 L10,8 L13,9 V11 Q12,13 10,13 Q2,11 1,3 Q1,1 3,1 Z" fill="#222"/></svg>000-000-0000</li>
      <li class="contact__line"><svg class="contact__icon" viewBox="0 0 14 14"><path d="M1,6 L7,1 L13,6 V13 H1 Z" fill="#222"/><path d="M2,6 L7,10 L12,6" fill="none" stroke="#fff" stroke-width="1.2"/></svg>abcde@abcdef.com</li>
      <li class="contact__line"><svg class="contact__icon" viewBox="0 0 14 14"><circle cx="7" cy="7" r="5.6" fill="none" stroke="#222" stroke-width="1.3"/><ellipse cx="7" cy="7" rx="2.4" ry="5.6" fill="none" stroke="#222" stroke-width="1.1"/><path d="M1.4,7 H12.6" stroke="#222" stroke-width="1.1"/></svg>www.abcdef.com</li>
    </ul>

    <div class="cta-bar">apply.vendrilux.com</div>
  </section>

</div>
</body>
</html>
```